Ebook cover for online appointment scheduling software

We are operating in Brazil an online appointment scheduling software offering small business to let their clients to book online with them . We nee...

Target Market(s)

Brazilian small businesses

Industry/Entity Type

Business Software

Requirements
Must have
• see the description
Nice to have
• see the description
Should not have
• see the description

```html
<!DOCTYPE html>
<html lang="pt-BR">
<head>
<meta charset="UTF-8">
<title>Agendamento Manual vs Agendamento Automatizado</title>
<link href="https://fonts.googleapis.com/css2?family=Barlow+Condensed:wght@500;600&display=swap" rel="stylesheet">
<style>
  :root {
    --red: #c9383d;
    --red-dark: #a92a30;
    --blue: #0b4ea6;
    --blue-light: #1566c8;
    --blue-dark: #062f78;
    --white: #ffffff;
    --figure-shade: #f1f1f3;
    --brand-grey: #5a5a5a;
  }
  html, body {
    margin: 0;
    padding: 0;
    width: 800px;
    height: 1200px;
    overflow: hidden;
  }
  .cover {
    position: relative;
    width: 800px;
    height: 1200px;
    overflow: hidden;
    font-family: "Barlow Condensed", "Arial Narrow", sans-serif;
    color: var(--white);
  }
  .side {
    position: absolute;
    top: 0;
    height: 1200px;
  }
  .side--manual {
    left: 0;
    width: 400px;
    background: radial-gradient(ellipse at 40% 35%, var(--red) 0%, var(--red) 55%, var(--red-dark) 100%);
  }
  .side--auto {
    left: 400px;
    width: 400px;
    background: radial-gradient(ellipse at 60% 30%, var(--blue-light) 0%, var(--blue) 45%, var(--blue-dark) 100%);
  }
  .tagline {
    position: absolute;
    top: 34px;
    left: 0;
    width: 800px;
    margin: 0;
    text-align: center;
    font-weight: 500;
    font-size: 34px;
    line-height: 46px;
    letter-spacing: 0.5px;
    text-transform: uppercase;
  }
  .heading {
    position: absolute;
    top: 312px;
    margin: 0;
    font-weight: 600;
    font-size: 64px;
    line-height: 76px;
    letter-spacing: 1px;
    text-transform: uppercase;
  }
  .heading--manual { left: 36px; }
  .heading--auto { left: 420px; }
  .boxers-illustration {
    position: absolute;
    left: 0;
    top: 580px;
    width: 800px;
    height: 620px;
  }
  .brand {
    position: absolute;
    right: 48px;
    bottom: 52px;
    display: flex;
    align-items: center;
    gap: 10px;
  }
  .brand__mark {
    width: 30px;
    height: 30px;
    border-radius: 50%;
    border: 3px solid var(--brand-grey);
    box-sizing: border-box;
  }
  .brand__name {
    font-weight: 500;
    font-size: 42px;
    line-height: 1;
    color: var(--brand-grey);
  }
</style>
</head>
<body>
  <div class="cover">
    <div class="side side--manual"></div>
    <div class="side side--auto"></div>

    <p class="tagline">Como agendar mais com menos tempo<br>e esforço ao usar o agendamento online</p>

    <h2 class="heading heading--manual">Agendamento<br>Manual</h2>
    <h2 class="heading heading--auto">Agendamento<br>Automatizado</h2>

    <svg class="boxers-illustration" viewBox="0 0 800 620" role="img" aria-label="Silhuetas brancas de dois boxeadores em confronto, um à esquerda sobre o fundo vermelho e outro à direita sobre o fundo azul">
      <defs>
        <linearGradient id="figureFill" x1="0" y1="0" x2="0" y2="1">
          <stop offset="0" stop-color="var(--white)"/>
          <stop offset="1" stop-color="var(--figure-shade)"/>
        </linearGradient>
      </defs>
      <path fill="url(#figureFill)"
            d="M20 620 C20 420 40 200 120 110 C170 60 250 60 300 150 C340 220 380 250 420 190 C470 110 560 100 640 170 C710 230 760 300 800 330 L800 620 Z"/>
    </svg>

    <div class="brand">
      <span class="brand__mark"></span>
      <span class="brand__name">Marcaflow</span>
    </div>
  </div>
</body>
</html>
```